We (R. T. Halvern & Associates, Inc.) are an executive Search firm based in Los Angeles that is exclusively focused in the Med Tech and Health Tech arenas.   I need a logo to communicate that we are a high end search firm, but also that we are focused in the medicine and science arenas called health tech and med tech.  Many of our clients have robotics and artificial intelligence type products, so it is very technology forward.  I tend to gravitate towards clean, sharp aesthetic as opposed to something that is really over the top.
Attached are files with my logo in two different layouts.  In addition to the letterhead and envelope, I also will need an electronic letterhead in Microsoft Word.  I tend to
I look forward to seeing the designs and just let me know if you have any questions.
Dale

```html
<!DOCTYPE html>
<html lang="en">
<head>
<meta charset="utf-8">
<title>R. T. Halvern &amp; Associates, Inc. — Stationery</title>
<link href="https://fonts.googleapis.com/css2?family=Source+Sans+3:wght@400;600&display=swap" rel="stylesheet">
<style>
  :root{
    --backdrop:#dcdcdc;
    --paper:#f1f2f4;
    --ink:#2b2b2b;
    --ink-soft:#4a4a4a;
    --brand-blue:#4a98d4;
    --envelope-dark:#262626;
    --flap-dark:#222222;
    --on-dark:#f4f4f4;
  }
  *{margin:0;padding:0;box-sizing:border-box}
  html,body{width:1200px;height:882px;overflow:hidden}
  body{background:var(--backdrop);font-family:"Source Sans 3",sans-serif;color:var(--ink);position:relative}

  .letterhead{position:absolute;left:93px;top:80px;width:499px;height:704px;background:var(--paper)}
  .brand{position:absolute;display:flex;align-items:center;gap:7px}
  .brand-dot{width:12px;height:12px;border-radius:50%;background:var(--brand-blue);flex:none}
  .brand-name{font-weight:600;color:var(--ink);line-height:1}
  .brand-name .line-main{display:block;font-size:15px;letter-spacing:.3px}
  .brand-name .line-sub{display:block;font-size:6px;letter-spacing:1.6px;margin-top:3px}
  .letterhead .brand{left:48px;top:60px}

  .header-address{position:absolute;left:190px;top:56px;width:117px;text-align:right;font-size:7.6px;line-height:10px;color:var(--ink-soft)}
  .header-address .firm{color:var(--brand-blue)}
  .header-divider{position:absolute;left:313px;top:58px;width:1px;height:28px;background:var(--ink-soft);opacity:.6}
  .header-contact{position:absolute;left:320px;top:56px;font-size:7.6px;line-height:10px;color:var(--ink-soft);list-style:none}
  .header-contact li{display:flex;align-items:center;gap:4px}
  .header-contact svg{width:6px;height:6px;fill:var(--brand-blue);flex:none}

  .letter-date{position:absolute;left:48px;top:176px;font-size:9px}
  .recipient{position:absolute;left:48px;top:212px;font-size:9px;line-height:12px;font-style:normal}
  .letter-body{position:absolute;left:47px;top:283px;width:404px;font-size:7.3px;line-height:12px;color:var(--ink-soft);text-align:justify}
  .letter-body p+p{margin-top:12px}
  .signature-mark{position:absolute;left:358px;top:529px;width:72px;height:34px;background:linear-gradient(90deg,#e4e5e8,#dcdde0);border-radius:3px}
  .signature-title{position:absolute;right:61px;top:557px;font-size:8px;color:var(--ink-soft)}

  .envelope{position:absolute;left:646px;width:472px}
  .envelope svg.flap{display:block;width:472px;height:68px}
  .envelope-body{height:215px;position:relative}
  .envelope--light{top:160px}
  .envelope--light .envelope-body{background:var(--paper)}
  .envelope--dark{top:501px}
  .envelope--dark .envelope-body{background:var(--envelope-dark)}
  .envelope--dark .brand-name{color:var(--on-dark)}
  .envelope .brand{left:30px;top:31px}
  .return-address{position:absolute;left:27px;top:168px;font-size:8px;line-height:10.5px;font-style:normal;color:var(--ink-soft)}
  .return-address .firm{color:var(--brand-blue);display:block}
  .envelope--dark .return-address{color:var(--on-dark)}
</style>
</head>
<body>

<section class="letterhead">
  <div class="brand">
    <span class="brand-dot"></span>
    <span class="brand-name"><span class="line-main">R. T. HALVERN</span><span class="line-sub">&amp; ASSOCIATES, INC.</span></span>
  </div>
  <address class="header-address" style="font-style:normal">
    <span class="firm">R.T.Halvern &amp; Associates Inc</span><br>
    1420 Larkspur Lane<br>
    Los Angeles, California 90017
  </address>
  <span class="header-divider"></span>
  <ul class="header-contact">
    <li><svg viewBox="0 0 10 10"><path d="M2 0l2 2-1 2c1 1 2 2 3 3l2-1 2 2-2 2C4 10 0 6 0 2z"/></svg>310-555-0142 &nbsp;310-555-0187</li>
    <li><svg viewBox="0 0 10 10"><path d="M0 2h10v6H0zM0 2l5 3 5-3"/></svg>info@rthalvernassociates.com</li>
    <li><svg viewBox="0 0 10 10"><circle cx="5" cy="5" r="5"/></svg>rthalvernassociates.com</li>
  </ul>

  <p class="letter-date">Cartagena de Indias, Ocober 12,2015</p>
  <address class="recipient">Sr.<br>TOMAS IBARRA<br>Web Master<br>City</address>

  <div class="letter-body">
    <p>Contrary to popular belief, Lorem Ipsum is not simply random text. It has roots in a piece of classical Latin literature from 45 BC, making it over 2000 years old. Ronald Fairbrook, a Latin professor at Harlow Ridge College in Vermont, looked up one of the more obscure Latin words, consectetur, from a Lorem Ipsum passage, and going through the cites of the word in classical literature,</p>
    <p>discovered the undoubtable source. Lorem Ipsum comes from sections 1.10.32 and 1.10.33 of "de Finibus Bonorum et Malorum" (The Extremes of Good and Evil) by Aurelian, written in 45 BC. This book is a treatise on the theory of ethics, very popular during the Renaissance. The first line of Lorem Ipsum, "Lorem ipsum dolor sit amet..", comes from a line in section 1.10.32.</p>
    <p>The standard chunk of Lorem Ipsum used since the 1500s is reproduced below for those interested. Sections 1.10.32 and 1.10.33 from "de Finibus Bonorum et Malorum" by Aurelian are also reproduced in their exact original form, accompanied by English versions from the 1914 translation by H. Lindqvist.</p>
    <p>There are many variations of passages of Lorem Ipsum available, but the majority have suffered alteration in some form, by injected humour, or randomised words which don't look even slightly believable. If you are going to use a passage of Lorem Ipsum, you need to be sure there isn't anything embarrassing hidden in the middle of text. All the Lorem Ipsum generators o</p>
  </div>
  <div class="signature-mark" role="img" aria-label="Handwritten signature of the founder"></div>
  <p class="signature-title">CEO/ FOUNDER</p>
</section>

<section class="envelope envelope--light">
  <svg class="flap" viewBox="0 0 472 68" preserveAspectRatio="none"><path d="M0 68 L10 22 Q14 0 36 0 H436 Q458 0 462 22 L472 68Z" fill="var(--brand-blue)"/></svg>
  <div class="envelope-body">
    <div class="brand">
      <span class="brand-dot"></span>
      <span class="brand-name"><span class="line-main">R. T. HALVERN</span><span class="line-sub">&amp; ASSOCIATES, INC.</span></span>
    </div>
    <address class="return-address"><span class="firm">R.T.Halvern &amp; Associates Inc.</span>1420 Larkspur Lane, California 90017</address>
  </div>
</section>

<section class="envelope envelope--dark">
  <svg class="flap" viewBox="0 0 472 68" preserveAspectRatio="none"><path d="M0 68 L10 22 Q14 0 36 0 H436 Q458 0 462 22 L472 68Z" fill="var(--flap-dark)"/></svg>
  <div class="envelope-body">
    <div class="brand">
      <span class="brand-dot"></span>
      <span class="brand-name"><span class="line-main">R. T. HALVERN</span><span class="line-sub">&amp; ASSOCIATES, INC.</span></span>
    </div>
    <address class="return-address"><span class="firm">R.T.Halvern &amp; Associates Inc.</span>1420 Larkspur Lane, California 90017</address>
  </div>
</section>

</body>
</html>
```